Plain, Clover is both an activist blog and personal health journey.

I am launching a blog. Ostensibly, as a platform for me to blog about my 17 year survival of multiple cancers. The US government has obscured the truth about cannabis for far too long, and I see plain clover as a platform, very Whitford-esque ... As in Elias Whitford, and plain Eli. Here, it is my nom de guerre, Dale Morrow. I want the look of the graphic splashes simple and clean and bold, ( Think Karl Penwick's design mentality) I have nothing to add or upload graphically, as I want you to interpret either your own views on the subject, or those of your interpretation of what other famous patriots ( yes, Dale Morrow will be a famous patriots someday) like ( fill in the blank ), got another idea? I'm open. Communicate. If you have a completely different idea about how to get neatt, concise platform page with windows for a video intro, ... Bla bla bla

Reason: I have nothing I feel strongly about yet.

Target Market(s)

Admittedly, the helpless and hopeless, sick and dying, addicted and disenfranchised; all because it just doesn't have to be that way.

Industry/Entity Type

Government

Font styles to use
Serif
Sans Serif
Decorative
Script

Requirements
Must have
• So far, I remain uninspired. Am I missing some questions from any or all of you?
Nice to have
• Make suggestionsplease communicate your ideas
Should not have
• please communicate your ideas

```html
<!DOCTYPE html>
<html lang="en">
<head>
<meta charset="utf-8">
<title>Plain Clover — Identity Sheet</title>
<link rel="stylesheet" href="https://fonts.googleapis.com/css2?family=Marcellus+SC&display=swap">
<style>
  :root {
    --paper: #ffffff;
    --ink: #231f20;
    --frame: #2e2a2b;
    --leaf-green: #5f9e58;
    --forest: #2f4434;
    --sand: #d6cdb7;
    --pale-green: #c9e3c1;
    --leaf-dark: #141414;
  }
  html, body {
    margin: 0;
    width: 1200px;
    height: 781px;
    overflow: hidden;
    background: var(--paper);
  }
  .sheet { display: block; width: 1200px; height: 781px; }
  .type { font-family: "Marcellus SC", "Copperplate", serif; }
  .card-frame { fill: var(--paper); stroke: var(--frame); stroke-width: 4; }
  .header-band { fill: #000; }
  .brand-name-light { fill: var(--pale-green); font-size: 38px; letter-spacing: 1px; }
  .brand-name-green { fill: var(--leaf-green); font-size: 60px; letter-spacing: 2px; }
  .brand-name-dark { fill: var(--ink); font-size: 60px; letter-spacing: 2px; }
  .brand-name-small { fill: var(--ink); font-size: 32px; letter-spacing: 1px; }
  .mark-dot { fill: var(--leaf-green); }
  .rule-fill { fill: var(--sand); }
  .triangle { fill: var(--leaf-green); stroke: var(--sand); stroke-width: 6; stroke-linejoin: miter; }
  .ornament-fill { fill: var(--sand); }
  .underline-fill { fill: var(--leaf-green); }
  .person { fill: var(--ink); font-size: 25px; letter-spacing: 1px; }
  .role { fill: var(--leaf-green); font-size: 12px; letter-spacing: .5px; }
  .detail { fill: var(--ink); font-size: 11.5px; letter-spacing: .4px; }
  .band-green { fill: var(--leaf-green); }
  .band-forest { fill: var(--forest); }
  .leaf-area { fill: var(--leaf-dark); }
</style>
</head>
<body>
<svg class="sheet type" viewBox="0 0 1200 781" xmlns="http://www.w3.org/2000/svg">

  <g class="card card-diagonal">
    <rect class="card-frame" x="48" y="3" width="530" height="299"/>
    <rect class="header-band" x="51" y="26" width="409" height="87"/>
    <text class="brand-name-light" x="84" y="80">Plain Clover</text>
    <circle class="mark-dot" cx="418" cy="67" r="11"/>
    <rect class="rule-fill" role="img" aria-label="Dotted rule ornament under the name"
          x="88" y="93" width="318" height="6" rx="3"/>

    <polygon class="triangle" points="276,302 575,102 575,302"/>
    <circle class="ornament-fill" role="img" aria-label="Ringed ornament on the diagonal"
            cx="458" cy="183" r="47"/>

    <text class="person" x="83" y="158">John Doe</text>
    <text class="role" x="83" y="171">Creative Art Director</text>
    <text class="detail" x="83" y="196">T: 555-555-5555</text>
    <text class="detail" x="83" y="209">W: yourdomain.com</text>
    <text class="detail" x="83" y="221">E: john@yourdomain.com</text>
    <text class="detail" x="83" y="247">Adress Line One</text>
    <text class="detail" x="83" y="260">Adress Line Two</text>
  </g>

  <g class="wordmark wordmark-ruled">
    <text class="brand-name-green" x="655" y="158">Plain Clover</text>
    <circle class="mark-dot" cx="1150" cy="138" r="20"/>
    <rect class="rule-fill" role="img" aria-label="Dotted rule ornament under the name"
          x="660" y="172" width="450" height="10" rx="5"/>
  </g>

  <g class="wordmark wordmark-underlined">
    <text class="brand-name-dark" x="48" y="662">Plain Clover</text>
    <rect class="underline-fill" role="img" aria-label="Tapered underline ornament"
          x="44" y="677" width="506" height="18"/>
  </g>

  <g class="card card-banded">
    <rect class="card-frame" x="656" y="481" width="530" height="298"/>
    <rect class="band-forest" x="660" y="484" width="224" height="9"/>
    <rect class="leaf-area" role="img" aria-label="Large dark leaf illustration along the left edge"
          x="658" y="484" width="92" height="293"/>

    <text class="brand-name-small" x="1153" y="553" text-anchor="end">Plain Clover</text>
    <rect class="underline-fill" role="img" aria-label="Tapered underline ornament"
          x="884" y="560" width="269" height="12"/>

    <text class="person" x="1145" y="640" text-anchor="end">John Doe</text>
    <text class="role" x="1145" y="653" text-anchor="end">Creative Art Director</text>
    <text class="detail" x="1145" y="677" text-anchor="end">T: 555-555-5555</text>
    <text class="detail" x="1145" y="690" text-anchor="end">W: yourdomain.com</text>
    <text class="detail" x="1145" y="703" text-anchor="end">E: john@yourdomain.com</text>

    <rect class="band-green" x="758" y="715" width="425" height="46"/>
    <text class="detail" x="1145" y="729" text-anchor="end">Adress Line One</text>
    <text class="detail" x="1145" y="742" text-anchor="end">Adress Line Two</text>
    <rect class="band-forest" x="777" y="761" width="406" height="16"/>
  </g>
</svg>
</body>
</html>
```